Radiant Crossing - An Exciting Mission & Book Cover Project

Help me to inspire people to live their best life! This is a mission, not just a design project.
I need a Book Cover designed to keep me inspired on the process of writing my book.
Book Title: Radiant Crossing
Tag Line: Three Simple Steps to get out of your own way, SuperCharge your Life and Step into Purpose!
Author: Marlis Quenby

The three steps are: Ownership, Vision and Action (Not sure if this should be on the front or back of the book cover)

The book is a self-help, motivational book. Personal development.
The cover needs to be strong and capture peoples attention, especially with competing shelf space. I almost see a fire ball of flame or explosion that will grab peoples attention.
My company is The Lantern Institute. I have added the company logo and a few pages of my presentation and topic outline to give an idea.
Maybe: The Lantern Institute logo on back of the cover. website is marlisquenby.com

THOUGHT: People should be able to take a photo of them holding the book cover showing what area of life they want Radiant Crossing in. This is why the front cover must be so visual and powerful that they want to take a photo with it. Ie. Explosion, fire, strong and bold.

Target Market(s)

Anyone who feels stuck and needs to breakthrough and move forward in life.

Industry/Entity Type

Motivation

Font styles to use
Serif
Sans Serif

Colors
ec1f27
f37122
fbed22

Requirements
Must have
• The design must be STRONG, SIMPLE, STAND OUT ON BOOK SHELVES.
Must have an open file to swap the photo and copy out.

Back Cover Page
1) Summary
2) 2-3 testimonials. One sentence.
3) About the Author (maybe with photo)
4) Lantern Institute logo
5) Website: radiantcrossing.com and marlisquenby.com
Nice to have
• If my photo works somewhere that would be great. I will change the photo later.
Added Where's Your Harbor? a nice cover example.
Should not have
• Right now I am writing the summary for the back of the cover. For now use Loreum Ipsum text and 2-3 recommendations. Again, I will get these only later.

```html
<!DOCTYPE html>
<html lang="en">
<head>
<meta charset="utf-8">
<title>Radiant Crossing — Marlis Quenby</title>
<link rel="stylesheet" href="https://fonts.googleapis.com/css2?family=Bebas+Neue&family=Cormorant+Garamond:ital,wght@1,500&family=Jost:wght@400;600&display=swap">
<style>
  :root {
    --page-bg: #ffffff;
    --cover-deep: #120403;
    --cover-ember: #3d0a06;
    --fire-red: #ec1f27;
    --fire-orange: #f37122;
    --fire-yellow: #fbed22;
    --fire-core: #fff8c4;
    --ink-light: #ffffff;
    --ink-soft: #fff3e6;
  }
  * { margin: 0; padding: 0; box-sizing: border-box; }
  html, body {
    width: 960px;
    height: 1200px;
    overflow: hidden;
    background: var(--page-bg);
  }
  .stage {
    position: relative;
    width: 960px;
    height: 1200px;
  }
  .book-cover {
    position: absolute;
    left: 107px;
    top: 40px;
    width: 746px;
    height: 1120px;
    overflow: hidden;
    background:
      radial-gradient(ellipse 65% 50% at 50% 48%, var(--cover-ember) 0%, #240604 60%, var(--cover-deep) 100%);
    box-shadow: 0 20px 50px rgba(0, 0, 0, 0.25);
  }
  .cover-illustration {
    position: absolute;
    left: 40px;
    top: 230px;
    width: 666px;
    height: 740px;
    background:
      radial-gradient(ellipse 48% 46% at 50% 50%,
        var(--fire-core) 0%,
        var(--fire-yellow) 10%,
        var(--fire-orange) 28%,
        rgba(236, 31, 39, 0.75) 46%,
        rgba(236, 31, 39, 0.25) 66%,
        rgba(236, 31, 39, 0) 82%);
  }
  .author-name {
    position: absolute;
    top: 100px;
    left: 0;
    width: 100%;
    text-align: center;
    font-family: "Cormorant Garamond", Georgia, serif;
    font-style: italic;
    font-weight: 500;
    font-size: 72px;
    line-height: 1;
    color: var(--ink-light);
  }
  .title-main {
    position: absolute;
    top: 330px;
    left: 0;
    width: 100%;
    text-align: center;
    font-family: "Bebas Neue", Impact, sans-serif;
    font-weight: 400;
    font-size: 205px;
    line-height: 1;
    letter-spacing: 10px;
    color: var(--ink-light);
    text-shadow: 0 0 28px rgba(60, 6, 2, 0.7);
  }
  .title-sub {
    position: absolute;
    top: 540px;
    left: 0;
    width: 100%;
    text-align: center;
    font-family: "Cormorant Garamond", Georgia, serif;
    font-style: italic;
    font-weight: 500;
    font-size: 100px;
    line-height: 1;
    color: var(--ink-light);
    text-shadow: 0 0 22px rgba(60, 6, 2, 0.75);
  }
  .tagline {
    position: absolute;
    top: 930px;
    left: 105px;
    right: 105px;
    text-align: center;
    font-family: "Jost", Arial, sans-serif;
    font-weight: 400;
    font-size: 30px;
    line-height: 1.3;
    color: var(--ink-soft);
  }
  .tagline strong { font-weight: 600; color: var(--ink-light); }
</style>
</head>
<body>
  <main class="stage">
    <section class="book-cover">
      <div class="cover-illustration" role="img" aria-label="Fiery explosion of red, orange and yellow light bursting outward"></div>
      <p class="author-name">Marlis Quenby</p>
      <h1 class="title-main">RADIANT</h1>
      <h2 class="title-sub">Crossing</h2>
      <p class="tagline">Three Simple Steps to get out of your own way, <strong>Super Charge your Life</strong> and Step into Purpose!</p>
    </section>
  </main>
</body>
</html>
```